Reef Lantern Tropical Fish Startup Design

I need professional business cards and social media profiles for our tropical fish shop.

Target Market(s)

Tropical fish enthusiasts

Industry/Entity Type

Tropical Fish

Font styles to use
Sans Serif
Script
Other font styles liked:
• Comforta

Colors
0054AA
0677BA
7BADD7
CADEEF
E8F1F8
0094D4
00A9DD
6FCCEA
C7EBF8
E9F6FB
00AB8E
00BBA5
67D7C9
C6EFE9
E9F9F6

Requirements
Must have
• fish, oceanic colors
Nice to have
• Lines, boxes, anything that groups the title to stand out
Should not have
• Any punctuations

```html
<!DOCTYPE html>
<html lang="en">
<head>
<meta charset="utf-8">
<title>Reef Lantern Business Card</title>
<link rel="stylesheet" href="https://fonts.googleapis.com/css2?family=Montserrat:wght@400;500;700&display=swap">
<style>
  :root {
    --page-bg: #e9f1f6;
    --ocean-deep: #003f80;
    --ocean: #0054aa;
    --ocean-mid: #0677ba;
    --sky: #00a9dd;
    --teal: #00ab8e;
    --teal-light: #67d7c9;
    --frost: #e9f6fb;
    --frost-glow: #c7ebf8;
    --text-light: #e9f6fb;
    --brand: #0054aa;
  }
  html, body {
    margin: 0;
    padding: 0;
    width: 1200px;
    height: 969px;
    overflow: hidden;
    background: var(--page-bg);
  }
  .card {
    position: absolute;
    left: 100px;
    top: 199px;
    width: 1000px;
    height: 571px;
    border-radius: 20px;
    overflow: hidden;
    background: radial-gradient(ellipse at 70% 40%, var(--frost-glow) 0%, var(--frost) 70%);
    box-shadow: 0 10px 30px rgba(0, 40, 90, 0.18);
    font-family: "Montserrat", sans-serif;
  }
  .card-shape {
    position: absolute;
    inset: 0;
  }
  .contact-block {
    position: absolute;
    left: 46px;
    top: 224px;
    color: var(--text-light);
  }
  .person-name {
    margin: 0;
    font-size: 29px;
    font-weight: 500;
    letter-spacing: 0.5px;
    text-transform: uppercase;
  }
  .person-role {
    margin: 2px 0 0;
    font-size: 21px;
    font-weight: 400;
  }
  .address {
    margin: 24px 0 0;
    font-size: 21px;
    line-height: 28px;
    font-weight: 400;
    letter-spacing: 0.3px;
  }
  .contact-list {
    list-style: none;
    margin: 18px 0 0;
    padding: 0;
    font-size: 21px;
    line-height: 28px;
    letter-spacing: 0.3px;
  }
  .contact-list li {
    display: flex;
    align-items: center;
    gap: 12px;
  }
  .contact-icon {
    width: 20px;
    height: 20px;
    fill: var(--text-light);
    flex: none;
  }
  .brand {
    position: absolute;
    left: 540px;
    top: 118px;
    width: 380px;
    display: flex;
    align-items: center;
    justify-content: center;
    gap: 20px;
  }
  .brand-emblem {
    width: 96px;
    height: 96px;
    border-radius: 50%;
    flex: none;
    background: radial-gradient(circle at 35% 35%, var(--teal-light) 0%, var(--sky) 55%, var(--ocean-mid) 100%);
  }
  .brand-name {
    margin: 0;
    color: var(--brand);
    font-size: 52px;
    line-height: 58px;
    font-weight: 700;
    text-transform: uppercase;
  }
</style>
</head>
<body>
  <div class="card">
    <svg class="card-shape" width="1000" height="571" viewBox="0 0 1000 571">
      <defs>
        <linearGradient id="oceanFill" x1="0" y1="0" x2="1" y2="1">
          <stop offset="0" stop-color="var(--ocean)"/>
          <stop offset="0.45" stop-color="var(--ocean-mid)"/>
          <stop offset="1" stop-color="var(--ocean-deep)"/>
        </linearGradient>
      </defs>
      <path d="M0 0 H335 C430 270 650 520 945 571 H0 Z" fill="url(#oceanFill)"/>
      <path d="M338 0 C436 272 656 520 950 566" fill="none" stroke="var(--teal)" stroke-width="4"/>
    </svg>

    <div class="brand">
      <div class="brand-emblem" role="img" aria-label="Tropical fish emblem"></div>
      <p class="brand-name">Reef<br>Lantern</p>
    </div>

    <div class="contact-block">
      <h1 class="person-name">Daniel Hart</h1>
      <p class="person-role">President</p>
      <p class="address">2140 Harbor Birch Road<br>Anchorage, Alaska 34820</p>
      <ul class="contact-list">
        <li>
          <svg class="contact-icon" viewBox="0 0 20 20"><path d="M4 2 L8 2 L9 6 L7 8 C8 11 9 12 12 13 L14 11 L18 12 L18 16 C18 17 17 18 16 18 C8 18 2 12 2 4 C2 3 3 2 4 2 Z"/></svg>
          369-480-1172
        </li>
        <li>
          <svg class="contact-icon" viewBox="0 0 20 20"><path d="M6 1 H14 A2 2 0 0 1 16 3 V17 A2 2 0 0 1 14 19 H6 A2 2 0 0 1 4 17 V3 A2 2 0 0 1 6 1 Z M6 3 V15 H14 V3 Z"/></svg>
          369-744-2093
        </li>
        <li>
          <svg class="contact-icon" viewBox="0 0 20 20"><path d="M5 2 H15 V7 H5 Z M2 8 H18 V15 H15 V18 H5 V15 H2 Z M7 13 V16 H13 V13 Z"/></svg>
          369-618-3540
        </li>
        <li>
          <svg class="contact-icon" viewBox="0 0 20 20"><path d="M2 5 H18 V15 H2 Z M3 6 L10 11 L17 6 Z" fill-rule="evenodd"/></svg>
          info@reeflantern.com
        </li>
        <li>
          <svg class="contact-icon" viewBox="0 0 20 20"><path d="M10 2 A8 8 0 1 0 10.01 2 Z M10 4 A6 6 0 1 1 9.99 4 Z M7 7 L11 6 L13 9 L10 13 L8 11 Z" fill-rule="evenodd"/></svg>
          www.reeflantern.com
        </li>
      </ul>
    </div>
  </div>
</body>
</html>
```